Laser Tattoo Removal Business Cards

We are looking for a professional business card design for a laser tattoo removal business. Ideally looking for a black business card design. The name of the business is Brightmoor Ink Erasure. We place our cards at local tattoo shops so we ideally are looking for something trendy/edgy to draw both male and female clientele in.

Target Market(s)

Male/Female ages 18-60

Contact Information for Business Card

black background ideally.. hoping to stay within greys, whites and black

Font styles to use
Serif
Sans Serif

Colors
121212
a9a9a9
5c5c5c
f5f5f5
ffffff
7f7f7f
606060
848484
9d9d9d

Requirements
Must have
• Employee Info:
• Melissa Danforth
• Chief Executive Offer
• m: 919.555.0143
• w: 919.555.0187
• f: 919.555.0162
• mdanforth@brightmoorinkerasure.com
• Address:
• 4518 Pell Ridge Dr, Suite 210
• Raleigh, NC 27699
• Website:
• www.brightmoorinkerasure.com
Nice to have
• Myabe business name on back or logo on back and employee info on the front

```html
<!DOCTYPE html>
<html lang="en">
<head>
<meta charset="utf-8">
<title>Brightmoor Ink Erasure – Business Cards</title>
<link href="https://fonts.googleapis.com/css2?family=Josefin+Sans:wght@400;600&family=Lato:wght@300;400;700&display=swap" rel="stylesheet">
<style>
  :root {
    --ink: #121212;
    --ink-soft: #1e1e1e;
    --paper: #ffffff;
    --paper-tint: #f5f5f5;
    --grey-light: #a9a9a9;
    --grey-mid: #7f7f7f;
    --grey-dark: #5c5c5c;
    --stage: #2a2a2a;
  }
  * { margin: 0; padding: 0; box-sizing: border-box; }
  html, body { width: 1200px; height: 900px; overflow: hidden; }
  body {
    background: var(--stage);
    font-family: "Lato", sans-serif;
    position: relative;
  }
  .card {
    position: absolute;
    width: 660px;
    height: 377px;
    border-radius: 3px;
    box-shadow: 0 18px 40px rgba(0,0,0,.55);
    overflow: hidden;
  }
  /* Back card */
  .card--back {
    left: 110px; top: 55px;
    background: var(--ink-soft);
    color: var(--paper);
    display: flex; flex-direction: column; align-items: center; justify-content: center;
  }
  .brand-name {
    font-family: "Josefin Sans", sans-serif;
    font-weight: 600;
    font-size: 40px;
    letter-spacing: 4px;
    text-transform: uppercase;
    display: flex; align-items: center; gap: 16px;
  }
  .brand-mark {
    width: 14px; height: 14px; background: currentColor; flex: none;
  }
  .brand-rule {
    width: 300px; height: 1px; background: currentColor; opacity: .6; margin-top: 18px;
  }
  .card--back .website {
    margin-top: 70px;
    font-size: 17px; letter-spacing: 2.5px; font-weight: 300;
  }
  /* Front card */
  .card--front {
    left: 430px; top: 470px;
    background: var(--paper);
    color: var(--ink);
  }
  .card--front .brand {
    position: absolute; left: 60px; top: 60px; width: 360px;
    display: flex; flex-direction: column; align-items: center;
  }
  .card--front .brand-name { font-size: 24px; letter-spacing: 2.5px; color: var(--ink); }
  .card--front .brand-mark { width: 10px; height: 10px; }
  .card--front .brand-rule { width: 220px; margin-top: 12px; background: var(--grey-dark); }
  .person {
    position: absolute; right: 56px; top: 62px;
    text-align: right; padding-right: 22px;
    border-right: 3px solid var(--ink);
    min-height: 150px;
  }
  .person__name { font-size: 17px; font-weight: 300; }
  .person__name strong { font-weight: 700; }
  .person__title { font-size: 12px; color: var(--grey-dark); margin-top: 3px; }
  .person__address { font-size: 14px; font-weight: 700; margin-top: 22px; line-height: 1.45; }
  .contact {
    position: absolute; left: 0; bottom: 58px;
    display: flex; align-items: stretch;
  }
  .contact__icons {
    background: var(--ink);
    border-radius: 0 14px 14px 0;
    padding: 12px 12px;
    display: flex; flex-direction: column; justify-content: space-between; gap: 10px;
  }
  .contact__icons svg { width: 16px; height: 16px; display: block; fill: var(--paper); }
  .contact__list {
    list-style: none; padding-left: 14px;
    display: flex; flex-direction: column; justify-content: space-between;
    font-size: 14px; color: var(--ink); letter-spacing: .3px;
  }
  .card__base { position: absolute; left: 0; bottom: 0; width: 660px; height: 70px; }
</style>
</head>
<body>

<section class="card card--back" aria-label="Card back">
  <div class="brand-name"><span class="brand-mark"></span>Brightmoor Ink Erasure</div>
  <div class="brand-rule"></div>
  <p class="website">www.brightmoorinkerasure.com</p>
</section>

<section class="card card--front" aria-label="Card front">
  <div class="brand">
    <div class="brand-name"><span class="brand-mark"></span>Brightmoor Ink Erasure</div>
    <div class="brand-rule"></div>
  </div>

  <div class="person">
    <p class="person__name">Melissa <strong>Danforth</strong></p>
    <p class="person__title">Chief Executive Offer</p>
    <p class="person__address">4518 Pell Ridge Dr, Suite 210<br>Raleigh, NC 27699</p>
  </div>

  <svg class="card__base" viewBox="0 0 660 70" aria-hidden="true">
    <rect x="0" y="52" width="660" height="18" fill="#a9a9a9"/>
    <path d="M380 52 L420 52 C440 52 440 20 470 20 L660 20 L660 70 L380 70 Z" fill="#121212"/>
  </svg>

  <div class="contact">
    <div class="contact__icons">
      <svg viewBox="0 0 16 16" aria-label="Phone"><path d="M2 5c0-2 2-3 6-3s6 1 6 3v1h-3V5H5v1H2zM4 7h8l2 6H2z"/></svg>
      <svg viewBox="0 0 16 16" aria-label="Mobile"><path d="M3 2l3-1 2 4-2 2c1 2 2 3 4 4l2-2 4 2-1 3c-7 1-13-5-12-12z"/></svg>
      <svg viewBox="0 0 16 16" aria-label="Fax"><path d="M4 1h8v4H4zM1 6h14v7h-3v2H4v-2H1zM5 10v4h6v-4z"/></svg>
      <svg viewBox="0 0 16 16" aria-label="Email"><path d="M1 3h14v10H1zM2 4l6 5 6-5z" fill-rule="evenodd"/></svg>
    </div>
    <ul class="contact__list">
      <li>919.555.0143</li>
      <li>919.555.0187</li>
      <li>919.555.0162</li>
      <li>mdanforth@brightmoorinkerasure.com</li>
    </ul>
  </div>
</section>

</body>
</html>
```